BrackenLeaf Billboards

We already hava a logo, slogan and general theme, we are looking for 2 to 3 billboard designs for out Recreational-Use Retail Cannabis Dispensary in NY state. We would like for the billboard to be a "Space" theme with a realistic-looking astronaut, we cannot have any "cartoon-like" images that would be attractive to children per state regulations. We would like the following wording included:
BrackenLeaf Cannabis Company - Oswego , slogan is "Products out of this world" , address of 287 Harlow Street - Oswego, Free Delivery - Orders over $150 . Our primary brand color is lime green.

```html
<!DOCTYPE html>
<html lang="en">
<head>
<meta charset="utf-8">
<title>BrackenLeaf Cannabis Company Billboard</title>
<link rel="stylesheet" href="https://fonts.googleapis.com/css2?family=Anton&family=Poppins:wght@600;700;800&display=swap">
<style>
  :root {
    --page: #2c3439;
    --board-dark: #0f1309;
    --board-mid: #2a3512;
    --lime: #c3dc22;
    --lime-soft: #a9c11c;
    --ink: #14180c;
    --white: #ffffff;
  }
  * { margin: 0; padding: 0; box-sizing: border-box; }
  html, body {
    width: 1200px;
    height: 857px;
    overflow: hidden;
    background: var(--page);
  }
  .billboard {
    position: absolute;
    left: 20px;
    top: 138px;
    width: 1160px;
    height: 580px;
    overflow: hidden;
    background:
      radial-gradient(ellipse 55% 70% at 78% 50%, var(--board-mid) 0%, rgba(42,53,18,0) 70%),
      var(--board-dark);
  }
  .astronaut-photo {
    position: absolute;
    left: 600px;
    top: 0;
    width: 560px;
    height: 580px;
    background:
      radial-gradient(ellipse 45% 60% at 55% 55%, #6f7d1f 0%, #4a5614 45%, rgba(30,38,10,0) 80%);
  }
  .brand {
    position: absolute;
    left: 98px;
    top: 46px;
    font-family: "Poppins", sans-serif;
    font-weight: 600;
    color: var(--white);
    line-height: 1.05;
  }
  .brand-name { display: block; font-size: 50px; letter-spacing: 1px; }
  .brand-sub { display: block; font-size: 27px; letter-spacing: 2px; margin-left: 18px; }
  .slogan-band {
    position: absolute;
    left: 0;
    top: 158px;
    width: 900px;
    height: 212px;
    background: linear-gradient(90deg, var(--lime) 0%, var(--lime) 55%, rgba(195,220,34,0) 100%);
  }
  .slogan {
    position: absolute;
    left: 50px;
    top: 160px;
    font-family: "Anton", sans-serif;
    font-size: 98px;
    line-height: 0.98;
    color: var(--white);
    text-transform: uppercase;
    letter-spacing: 1px;
    -webkit-text-stroke: 9px var(--ink);
    paint-order: stroke fill;
  }
  .address-band {
    position: absolute;
    left: 0;
    top: 370px;
    width: 820px;
    height: 50px;
    background: linear-gradient(90deg, var(--ink) 0%, var(--ink) 70%, rgba(20,24,12,0) 100%);
  }
  .address {
    position: absolute;
    left: 50px;
    top: 383px;
    font-family: "Poppins", sans-serif;
    font-weight: 700;
    font-size: 20px;
    color: var(--white);
    text-transform: uppercase;
  }
  .offer-band {
    position: absolute;
    left: 0;
    top: 420px;
    width: 860px;
    height: 108px;
    background: linear-gradient(90deg, var(--lime) 0%, var(--lime-soft) 50%, rgba(169,193,28,0) 100%);
  }
  .offer {
    position: absolute;
    left: 52px;
    top: 428px;
    display: flex;
    align-items: center;
    gap: 18px;
    font-family: "Poppins", sans-serif;
    font-weight: 800;
    color: var(--ink);
    text-transform: uppercase;
    line-height: 0.95;
  }
  .offer-free .big { display: block; font-size: 58px; letter-spacing: 1px; }
  .offer-free .small { display: block; font-size: 29px; }
  .offer-min { font-size: 43px; }
</style>
</head>
<body>
  <main class="billboard">
    <div class="astronaut-photo" role="img" aria-label="Realistic astronaut in a spacesuit pointing toward the slogan, tinted lime green, with drifting rock fragments and star dust"></div>

    <div class="brand">
      <span class="brand-name">BrackenLeaf</span>
      <span class="brand-sub">CANNABIS COMPANY</span>
    </div>

    <div class="slogan-band"></div>
    <h1 class="slogan">Products out<br>of this world</h1>

    <div class="address-band"></div>
    <p class="address">Address of 287 Harlow Street – Oswego</p>

    <div class="offer-band"></div>
    <div class="offer">
      <div class="offer-free"><span class="big">Free</span><span class="small">Delivery</span></div>
      <div class="offer-min">Orders<br>over $150</div>
    </div>
  </main>
</body>
</html>
```